Hockey Sponsorship Proposal

We are looking for a sponsorship proposal design for an apparel company to supply our hockey camps with jerseys and apparel. We want to use lots of visuals so potential business partners can see the exposure and publicity their company could get by working with us. We would like the primary colors to be red, black and white. We have attached a bunch of images but not all need to be used. We would like to see a mix of images with adult players and youth players where appropriate. Although I have provided a rough outline for the information on the powerpoint the text and images can be displayed however you would like.

Here is a link to some proposals to give you an idea of what we are looking for
https://www.quillrack.co.uk/pin/512604837219056471/

Target Market(s)

Athletic Apparel Companies

Industry/Entity Type

It Company

Requirements
Must have
• Please note this should be suitable for web as the proposal will be emailed. This is NOT for print.
Nice to have
• I would like the first page to have a full image as the backdrop with the text over top if possible.

```html
<!DOCTYPE html>
<html lang="en">
<head>
<meta charset="utf-8">
<title>About Warren Halloway</title>
<link href="https://fonts.googleapis.com/css2?family=Oswald:wght@400;500;600&family=Arimo:wght@400;700&display=swap" rel="stylesheet">
<style>
  :root {
    --stage: #c9c9c9;
    --sheet: #ffffff;
    --navy: #1f2d4e;
    --red: #c40d12;
    --grey-text: #6b6b6b;
    --link: #1a0dab;
    --link-visited: #660099;
    --source: #006621;
    --snippet: #545454;
  }
  * { margin: 0; padding: 0; box-sizing: border-box; }
  html, body { width: 1200px; height: 1000px; overflow: hidden; }
  body { background: var(--stage); position: relative; font-family: "Oswald", sans-serif; }

  .slide {
    position: absolute; left: 18px; top: 113px; width: 1163px; height: 773px;
    background: var(--sheet);
    box-shadow: 0 2px 8px rgba(0,0,0,0.35);
  }
  .title-banner { position: absolute; left: 20px; top: 191px; }
  .slide-title {
    position: absolute; left: 90px; top: 194px;
    font-family: "Oswald", sans-serif; font-weight: 500;
    font-size: 58px; line-height: 74px; color: #ffffff; letter-spacing: 0.3px;
    white-space: nowrap;
  }

  .highlights { list-style: none; }
  .highlight { position: absolute; left: 0; width: 520px; }
  .highlight::before {
    content: ""; position: absolute; left: 20px; top: 4px;
    width: 53px; height: 33px; background: var(--red);
  }
  .highlight p {
    margin-left: 87px; font-weight: 500; font-size: 23px; line-height: 34px;
    color: var(--navy); width: 405px;
  }
  .h1 { top: 328px; } .h2 { top: 501px; } .h3 { top: 603px; }

  .more {
    position: absolute; left: 54px; top: 804px;
    font-weight: 500; font-size: 20px; color: var(--grey-text);
  }
  .more strong { color: var(--navy); font-weight: 500; margin-left: 6px; }

  .media-heading {
    position: absolute; left: 760px; width: 322px; top: 298px; text-align: center;
    font-weight: 500; font-size: 30px; color: var(--navy);
  }
  .media-item { position: absolute; left: 537px; width: 640px; height: 116px; }
  .media-item svg { position: absolute; left: 0; top: 0; }
  .media-text { position: absolute; left: 165px; top: 27px; width: 455px; font-family: "Arimo", Arial, sans-serif; }
  .media-title { font-size: 14px; line-height: 18px; color: var(--link); white-space: nowrap; overflow: hidden; }
  .media-title.visited { color: var(--link-visited); }
  .media-source { font-size: 12.5px; line-height: 16px; color: var(--source); }
  .media-source span { color: #808080; }
  .media-snippet { font-size: 12.3px; line-height: 15px; color: var(--snippet); }
  .m1 { top: 337px; } .m2 { top: 462px; } .m3 { top: 592px; } .m4 { top: 717px; }
  .media-item.m3 .media-text, .media-item.m4 .media-text { left: 161px; }
</style>
</head>
<body>
  <main class="slide"></main>

  <svg class="title-banner" width="800" height="80" viewBox="0 0 800 80" aria-hidden="true">
    <polygon points="40,0 800,0 760,80 0,80" fill="var(--navy)"/>
  </svg>
  <h1 class="slide-title">ABOUT WARREN HALLOWAY</h1>

  <ul class="highlights">
    <li class="highlight h1"><p>Preeminent performance coach for many of the PHL’s biggest superstars including Tomas Varden, Marek Lindqvist &amp; Owen Strathy.</p></li>
    <li class="highlight h2"><p>Player Development Consultant for the Lakeshore Wolverines.</p></li>
    <li class="highlight h3"><p>Regarded as an innovator and leading expert in uncovering new pathways of performance excellence.</p></li>
  </ul>

  <p class="more">For more on Warren please visit <strong>hallowayhockey.com</strong></p>

  <h2 class="media-heading">WARREN IN THE MEDIA</h2>

  <article class="media-item m1">
    <svg width="162" height="116" viewBox="0 0 162 116" role="img" aria-label="Photo: coach instructing young players on the ice">
      <defs><linearGradient id="rink1" x1="0" y1="0" x2="0" y2="1"><stop offset="0" stop-color="#2f5fb0"/><stop offset="0.55" stop-color="#d9e2ec"/><stop offset="1" stop-color="#6b7180"/></linearGradient></defs>
      <polygon points="40,0 152,0 114,112 0,112" fill="var(--red)"/>
      <polygon points="46,6 160,6 122,116 8,116" fill="url(#rink1)"/>
    </svg>
    <div class="media-text">
      <p class="media-title">Wolverines teammates break down Owen Strathy' unique shooting ...</p>
      <p class="media-source">Rinkwire.ca <span>- Oct 19, 2017</span></p>
      <p class="media-snippet">According to Strathy' father Gary, much of that unpredictable style can be credited to skills coach <b>Warren Halloway</b>, who's worked with the ...</p>
    </div>
  </article>

  <article class="media-item m2">
    <svg width="162" height="116" viewBox="0 0 162 116" role="img" aria-label="Photo: coach talking with a player in a red jersey">
      <defs><linearGradient id="rink2" x1="0" y1="0" x2="1" y2="0"><stop offset="0" stop-color="#b3272a"/><stop offset="0.5" stop-color="#c9b89a"/><stop offset="1" stop-color="#3a3a3e"/></linearGradient></defs>
      <polygon points="40,0 152,0 114,112 0,112" fill="var(--red)"/>
      <polygon points="46,6 160,6 122,116 8,116" fill="url(#rink2)"/>
    </svg>
    <div class="media-text">
      <p class="media-title visited">From Marek Lindqvist on down, <b>Warren Halloway</b> driven to develop ...</p>
      <p class="media-source">The Slot Report <span>- May 9, 2017</span></p>
      <p class="media-snippet">Performance coach <b>Warren Halloway</b> is known best for the work he's done with some of the PHL's biggest stars of today. From Tomas Varden to ...</p>
    </div>
  </article>

  <article class="media-item m3">
    <svg width="162" height="116" viewBox="0 0 162 116" role="img" aria-label="Photo: coach pointing while a player in a gold jersey listens">
      <defs><linearGradient id="rink3" x1="0" y1="0" x2="1" y2="1"><stop offset="0" stop-color="#e0b43a"/><stop offset="0.5" stop-color="#9c8a6e"/><stop offset="1" stop-color="#2b2b2e"/></linearGradient></defs>
      <polygon points="40,0 152,0 114,112 0,112" fill="var(--red)"/>
      <polygon points="46,6 160,6 122,116 8,116" fill="url(#rink3)"/>
    </svg>
    <div class="media-text">
      <p class="media-title">Wolverines skills coach <b>Warren Halloway</b> part of new philosophy</p>
      <p class="media-source">Blue Line Notes <span>- May 25, 2015</span></p>
      <p class="media-snippet">As the Wolverines rebuild gets underway, the team's newest skill development coach is just getting started. I had the chance to chat with <b>Warren Halloway</b> ...</p>
    </div>
  </article>

  <article class="media-item m4">
    <svg width="162" height="116" viewBox="0 0 162 116" role="img" aria-label="Photo: coach on the ice beside a player in a white practice jersey">
      <defs><linearGradient id="rink4" x1="0" y1="0" x2="0" y2="1"><stop offset="0" stop-color="#4a4a52"/><stop offset="0.5" stop-color="#e6e6e6"/><stop offset="1" stop-color="#b9bfc7"/></linearGradient></defs>
      <polygon points="40,0 152,0 114,112 0,112" fill="var(--red)"/>
      <polygon points="46,6 160,6 122,116 8,116" fill="url(#rink4)"/>
    </svg>
    <div class="media-text">
      <p class="media-title visited">PHL star players descend on Coral Ice Centre to train with Bayside ...</p>
      <p class="media-source">The Harbor Ledger <span>- Sep 4, 2017</span></p>
      <p class="media-snippet">For 25 years, <b>Warren Halloway</b> has been fascinated with the science of hockey. From replaying grainy tapes of 'Saturday Night Hockey' games to ...</p>
    </div>
  </article>
</body>
</html>
```